We want a business card/punch card for our business. We are including examples of our current business card (we like the front of our business card and not looking to remake it). We need only back side to be designed in form of a punch card (we are including a sample of the punch card we made, but are unsatisfied). For each $180 spend (9 punches) our clients have $20 off.

Colors
886aae

```html
<!DOCTYPE html>
<html lang="en">
<head>
<meta charset="utf-8">
<title>Lotus Path Appreciation Card</title>
<link href="https://fonts.googleapis.com/css2?family=Dancing+Script:wght@500;600;700&display=swap" rel="stylesheet">
<style>
  :root {
    --stage: #2a2a2e;
    --brand-purple: #886aae;
    --band-violet: #7a3fc4;
    --band-blue: #4d6fd8;
    --card-dark: #18181c;
    --ink-purple: #6a2fc0;
    --ink-grey: #555560;
    --title-silver: #cfcfd4;
    --slot-fill: #8fa3ea;
    --slot-ring: #dfe4fb;
    --slot-ink: #2d2a6e;
  }
  * { margin: 0; padding: 0; box-sizing: border-box; }
  html, body { width: 1200px; height: 900px; overflow: hidden; }
  body {
    background: var(--stage);
    font-family: "Dancing Script", cursive;
    display: flex;
    flex-direction: column;
    align-items: center;
    justify-content: center;
    gap: 46px;
  }
  .card {
    position: relative;
    width: 660px;
    height: 377px;
    border-radius: 22px;
    overflow: hidden;
    box-shadow: 0 10px 30px rgba(0,0,0,.45);
  }
  .card-art { position: absolute; inset: 0; width: 100%; height: 100%; }

  /* message side */
  .brand {
    position: absolute;
    left: 40px;
    top: 150px;
    display: flex;
    align-items: center;
    gap: 10px;
    color: var(--ink-grey);
    font-size: 40px;
    font-weight: 600;
  }
  .brand-dot {
    width: 22px; height: 22px;
    border-radius: 50%;
    background: var(--brand-purple);
  }
  .message {
    position: absolute;
    left: 270px;
    top: 86px;
    width: 360px;
    color: var(--ink-purple);
    font-size: 19px;
    font-weight: 500;
    line-height: 1.15;
  }
  .website {
    position: absolute;
    left: 330px;
    top: 282px;
    display: flex;
    align-items: center;
    gap: 10px;
    color: var(--ink-purple);
    font-size: 21px;
    font-weight: 500;
  }
  .globe-icon { width: 26px; height: 26px; }

  /* punch side */
  .title-block {
    position: absolute;
    left: 0; right: 0;
    top: 142px;
    text-align: center;
    transform: rotate(-8deg);
  }
  .card-title {
    color: var(--title-silver);
    font-size: 46px;
    font-weight: 500;
    line-height: 1.1;
  }
  .punch-rule {
    margin-top: 6px;
    color: var(--slot-fill);
    font-size: 21px;
    font-weight: 600;
  }
  .slot-number {
    font-family: "Dancing Script", cursive;
    font-size: 22px;
    font-weight: 700;
    fill: var(--slot-ink);
  }
</style>
</head>
<body>

  <section class="card card-message">
    <svg class="card-art" viewBox="0 0 660 377" aria-hidden="true">
      <defs>
        <radialGradient id="paper" cx="55%" cy="45%" r="75%">
          <stop offset="0" stop-color="#ffffff"/>
          <stop offset="1" stop-color="#c8c5e6"/>
        </radialGradient>
      </defs>
      <rect width="660" height="377" fill="url(#paper)"/>
      <path d="M0 0 H660 V34 Q330 58 0 26 Z" fill="#7a3fc4"/>
      <path d="M0 0 H660 V24 Q330 46 0 18 Z" fill="#4d6fd8"/>
      <path d="M0 377 V340 Q330 322 660 350 V377 Z" fill="#7a3fc4"/>
      <path d="M0 377 V350 Q330 334 660 360 V377 Z" fill="#4d6fd8"/>
    </svg>

    <div class="brand"><span class="brand-dot"></span>Lotus Path</div>

    <p class="message">This card is a symbol of appreciation from us to you, without your business we would not be able to do what we love most. When you fillout this card, you will receive $20 toward your next Weekly event, Workshop or Private event.</p>

    <div class="website">
      <svg class="globe-icon" viewBox="0 0 26 26" aria-hidden="true">
        <circle cx="13" cy="13" r="12" fill="#6a2fc0"/>
        <ellipse cx="13" cy="13" rx="5" ry="11" fill="none" stroke="#fff" stroke-width="1.4"/>
        <line x1="2" y1="13" x2="24" y2="13" stroke="#fff" stroke-width="1.4"/>
      </svg>
      www.LotusPathStudio.com
    </div>
  </section>

  <section class="card card-punch">
    <svg class="card-art" viewBox="0 0 660 377" aria-hidden="true">
      <rect width="660" height="377" fill="#18181c"/>
      <path d="M0 0 H660 V24 C450 38 220 76 0 120 Z" fill="#7a3fc4"/>
      <path d="M0 377 V352 C240 330 450 292 660 250 V377 Z" fill="#7a3fc4"/>
    </svg>
    <svg class="card-art punch-slots" viewBox="0 0 660 377" role="img" aria-label="Nine punch slots, one for every $20 spent">
      <g fill="#8fa3ea" stroke="#dfe4fb" stroke-width="2.5">
        <circle cx="50" cy="113" r="26"/>
        <circle cx="185" cy="93" r="26"/>
        <circle cx="320" cy="73" r="26"/>
        <circle cx="455" cy="54" r="26"/>
        <circle cx="590" cy="36" r="26"/>
        <circle cx="105" cy="334" r="26"/>
        <circle cx="250" cy="312" r="26"/>
        <circle cx="395" cy="290" r="26"/>
        <circle cx="540" cy="268" r="26"/>
      </g>
      <g class="slot-number" text-anchor="middle" dominant-baseline="central">
        <text x="50" y="113">1</text>
        <text x="185" y="93">2</text>
        <text x="320" y="73">3</text>
        <text x="455" y="54">4</text>
        <text x="590" y="36">5</text>
        <text x="105" y="334">6</text>
        <text x="250" y="312">7</text>
        <text x="395" y="290">8</text>
        <text x="540" y="268">9</text>
      </g>
    </svg>
    <div class="title-block">
      <h1 class="card-title">Lotus Path Appreciation Card</h1>
      <p class="punch-rule">One punch per $20 spent · 9 punches ($180) = $20 off</p>
    </div>
  </section>

</body>
</html>
```